Boutique personal training and fitness studio - banner ad design

We need a 'revolving' banner ad designed for our personal training and fitness studio. There are three separate offers (i.e. 3 pages to the advertisements)
Offer 1
PT Starter Pack
3 personal training sessions
$119
New clients only
Offer 2
Group fitness
2 weeks unlimited group fitness classes
$29
New clients only
Offer 3
Strength starter pack
2 weeks unlimited group fitness classes and 2 PT sessions
$89
New clients only
Please do not put the words "Offer 1, 2 or 3" in the ads - just the text following each offer.
Each advertisement should be sized to fit across around half of the webpage and be in landscape format.
Each advertisement should have a suitable picture (no cartoons) and should be complimentary to the existing website.
Each advertisement should also include the logo (attached)
www.harrowdaleliftroom.com.au
Training

```html
<!DOCTYPE html>
<html lang="en">
<head>
<meta charset="utf-8">
<title>Strength Starter Pack – Banner Ads</title>
<link rel="stylesheet" href="https://fonts.googleapis.com/css2?family=Oswald:wght@500;700&family=Tinos&display=swap">
<style>
  :root {
    --stage-bg: #8a5a35;
    --heading-light: #ffffff;
    --panel-dark: #1f1f1f;
    --divider: #e9e9e9;
    --headline-light: #ffffff;
    --offer-cream: #f4eed3;
    --teal: #2f6177;
    --teal-deep: #234b5d;
    --red: #d81f26;
    --ribbon-grey: #c4c4c4;
    --ink-dark: #222222;
    --logo-silver: #d6d6d6;
    --logo-grey: #4a4a4a;
  }
  html, body {
    margin: 0;
    padding: 0;
    width: 1200px;
    height: 967px;
    overflow: hidden;
    background: var(--stage-bg);
  }
  .banner-set {
    position: relative;
    width: 1200px;
    height: 967px;
  }
  .set-title {
    position: absolute;
    left: 227px;
    top: 22px;
    margin: 0;
    font-family: "Oswald", sans-serif;
    font-weight: 500;
    font-size: 46px;
    line-height: 1;
    color: var(--heading-light);
  }
  .banner {
    position: absolute;
    left: 227px;
    width: 780px;
    height: 388px;
    display: block;
    box-shadow: 0 4px 14px rgba(0,0,0,0.35);
  }
  .banner--teal { top: 99px; }
  .banner--red { top: 512px; }
  .headline {
    font-family: "Oswald", sans-serif;
    font-weight: 700;
  }
  .subhead {
    font-family: "Oswald", sans-serif;
    font-weight: 700;
    fill: var(--headline-light);
  }
  .offer-line {
    font-family: "Oswald", sans-serif;
    font-weight: 700;
    font-size: 27px;
    fill: var(--offer-cream);
  }
  .price {
    font-family: "Oswald", sans-serif;
    font-weight: 500;
    font-size: 40px;
    fill: #ffffff;
  }
  .ribbon-text {
    font-family: "Tinos", serif;
    font-size: 25px;
  }
  .ribbon-text--light { fill: #ffffff; }
  .ribbon-text--dark { fill: var(--ink-dark); }
  .brand-name {
    font-family: "Oswald", sans-serif;
    font-weight: 700;
    font-size: 19px;
  }
  .brand-name--light { fill: var(--logo-silver); }
  .brand-name--dark { fill: var(--logo-grey); }
  .photo-frame {
    fill: none;
    stroke-width: 2;
    stroke-dasharray: 10 7;
  }
  .photo-frame--light { stroke: rgba(255,255,255,0.55); }
  .photo-frame--dark { stroke: rgba(60,60,60,0.35); }
  .photo-icon--light { stroke: rgba(255,255,255,0.6); fill: none; stroke-width: 4; }
  .photo-icon--dark { stroke: rgba(60,60,60,0.4); fill: none; stroke-width: 4; }
</style>
</head>
<body>
<main class="banner-set">

  <h1 class="set-title">OFFER 3</h1>

  <svg class="banner banner--teal" viewBox="0 0 780 388" xmlns="http://www.w3.org/2000/svg">
    <defs>
      <linearGradient id="tealPhoto" x1="0" y1="0" x2="1" y2="1">
        <stop offset="0" stop-color="#8cc0cc"/>
        <stop offset="0.5" stop-color="#4d8597"/>
        <stop offset="1" stop-color="#1e3f4d"/>
      </linearGradient>
      <linearGradient id="silverA" x1="0" y1="0" x2="0" y2="1">
        <stop offset="0" stop-color="#ffffff"/>
        <stop offset="0.5" stop-color="#cfcfcf"/>
        <stop offset="0.55" stop-color="#9a9a9a"/>
        <stop offset="1" stop-color="#e8e8e8"/>
      </linearGradient>
    </defs>
    <rect class="panel" x="0" y="0" width="780" height="388" fill="var(--panel-dark)"/>
    <g role="img" aria-label="Photo of a fit man and woman holding dumbbells against a teal background">
      <polygon points="0,0 498,0 344,388 0,388" fill="url(#tealPhoto)"/>
      <polygon class="photo-frame photo-frame--light" points="14,14 478,14 335,374 14,374"/>
      <g class="photo-icon--light" transform="translate(200,175)">
        <rect x="-46" y="-34" width="92" height="68" rx="6"/>
        <circle cx="-20" cy="-12" r="8"/>
        <polyline points="-40,26 -10,-2 8,14 22,2 40,26"/>
      </g>
    </g>
    <polygon class="divider" points="498,0 512,0 358,388 344,388" fill="var(--divider)"/>

    <text class="headline" x="757" y="106" text-anchor="end" font-size="64" fill="url(#silverA)" textLength="258" lengthAdjust="spacingAndGlyphs">STRENGTH</text>
    <text class="subhead" x="757" y="157" text-anchor="end" font-size="40" textLength="258" lengthAdjust="spacingAndGlyphs">STARTER PACK</text>

    <text class="offer-line" x="760" y="206" text-anchor="end">2 WEEKS UNLIMITED</text>
    <text class="offer-line" x="760" y="235" text-anchor="end">GROUP FITNESS CLASSES</text>
    <text class="offer-line" x="760" y="264" text-anchor="end">AND 2 PT SESSIONS</text>

    <polygon class="ribbon" points="478,293 780,293 780,340 494,340" fill="var(--teal)"/>
    <text class="ribbon-text ribbon-text--light" x="771" y="325" text-anchor="end">NEW CLIENTS ONLY!</text>

    <circle class="price-badge" cx="380" cy="307" r="52" fill="#ffffff" opacity="0.9"/>
    <circle class="price-badge" cx="380" cy="307" r="48" fill="var(--teal-deep)"/>
    <text class="price" x="380" y="322" text-anchor="middle">$89</text>

    <text class="brand-name brand-name--light" x="14" y="349">HARROWDALE</text>
    <text class="brand-name brand-name--light" x="14" y="372">LIFT ROOM</text>
  </svg>

  <svg class="banner banner--red" viewBox="0 0 780 388" xmlns="http://www.w3.org/2000/svg">
    <defs>
      <linearGradient id="greyPhoto" x1="0" y1="0" x2="1" y2="1">
        <stop offset="0" stop-color="#f1f1f1"/>
        <stop offset="0.6" stop-color="#d8d9db"/>
        <stop offset="1" stop-color="#b9b9bb"/>
      </linearGradient>
      <linearGradient id="silverB" x1="0" y1="0" x2="0" y2="1">
        <stop offset="0" stop-color="#ffffff"/>
        <stop offset="0.5" stop-color="#cfcfcf"/>
        <stop offset="0.55" stop-color="#9a9a9a"/>
        <stop offset="1" stop-color="#e8e8e8"/>
      </linearGradient>
    </defs>
    <rect class="panel" x="0" y="0" width="780" height="388" fill="var(--panel-dark)"/>
    <g role="img" aria-label="Photo of a muscular woman seen from behind lifting a red dumbbell on a light grey background">
      <polygon points="0,0 498,0 344,388 0,388" fill="url(#greyPhoto)"/>
      <polygon class="photo-frame photo-frame--dark" points="14,14 478,14 335,374 14,374"/>
      <g class="photo-icon--dark" transform="translate(180,200)">
        <rect x="-46" y="-34" width="92" height="68" rx="6"/>
        <circle cx="-20" cy="-12" r="8"/>
        <polyline points="-40,26 -10,-2 8,14 22,2 40,26"/>
      </g>
    </g>
    <polygon class="divider" points="498,0 512,0 358,388 344,388" fill="var(--divider)"/>

    <text class="headline" x="757" y="106" text-anchor="end" font-size="64" fill="url(#silverB)" textLength="258" lengthAdjust="spacingAndGlyphs">STRENGTH</text>
    <text class="subhead" x="757" y="157" text-anchor="end" font-size="40" textLength="258" lengthAdjust="spacingAndGlyphs">STARTER PACK</text>

    <text class="offer-line" x="760" y="206" text-anchor="end">2 WEEKS UNLIMITED</text>
    <text class="offer-line" x="760" y="235" text-anchor="end">GROUP FITNESS CLASSES</text>
    <text class="offer-line" x="760" y="264" text-anchor="end">AND 2 PT SESSIONS</text>

    <polygon class="ribbon" points="478,293 780,293 780,340 494,340" fill="var(--ribbon-grey)"/>
    <text class="ribbon-text ribbon-text--dark" x="771" y="325" text-anchor="end">NEW CLIENTS ONLY!</text>

    <circle class="price-badge" cx="380" cy="307" r="52" fill="#ffffff"/>
    <circle class="price-badge" cx="380" cy="307" r="48" fill="var(--red)"/>
    <text class="price" x="380" y="322" text-anchor="middle">$89</text>

    <text class="brand-name brand-name--dark" x="318" y="48">HARROWDALE</text>
    <text class="brand-name brand-name--dark" x="318" y="71">LIFT ROOM</text>
  </svg>

</main>
</body>
</html>
```